Business Cards/Stationary for New Travel Agency
Bright Compass Travel
Business Cards/Stationary for New Travel Agency - Travel
Creative Brief
Professional
Melvor Tansley
Leisure and Business Travel Agent
OakVale Court Office, 418 Brindle Blvd., 4th Floor, Santa Monica, CA, 90408 Tel: 310-555-0193 Go Yonder Office, 526 Fenwick Ave., #C, Santa Monica, CA, 90406 Tel: 310-555-0147 ext. 3871
melvor@brightcompasstravelagency.example
www.brightcompasstravelagency.example
Go Yonder Affiliate - CST# 2937516-82
Contact information for both addresses needed on front of business cards. (Two separate columns with each address may look better.) Font size should be big as possible without looking too crowded. Affiliate/License No. can be in small print on bottom of business cards.
Logo on white background. (Big)
drumreed drumreed
loverdan loverdan
#80 - On the back, can you please change Go Yonder Affiliate to Cobble Tours Affiliate and make the font size bigger? Can you please make the font size bigger for the front of the card? (When I adjust the card on the screen to actual size, the font size is too small which will make it difficult for older people to read.)
To all designers: Please upload business card design in mock-up/printer-ready format to see actual size and text. Thank you!!

```html
<!DOCTYPE html>
<html lang="en">
<head>
<meta charset="utf-8">
<title>Bright Compass Travel – Stationery</title>
<link href="https://fonts.googleapis.com/css2?family=Open+Sans:wght@400;600;700&display=swap" rel="stylesheet">
<style>
  :root {
    --navy: #1c325e;
    --navy-deep: #14264a;
    --gold: #f2a81d;
    --paper: #ffffff;
    --stage: #eeeff1;
    --ink: #4a5160;
    --ink-soft: #8a909c;
    --brand: #1c325e;
  }
  * { box-sizing: border-box; margin: 0; padding: 0; }
  html, body { width: 1200px; height: 370px; overflow: hidden; }
  body {
    background: var(--stage);
    font-family: "Open Sans", Arial, sans-serif;
    color: var(--ink);
    position: relative;
  }
  .piece {
    position: absolute;
    background: var(--paper);
    box-shadow: 0 2px 6px rgba(0,0,0,.15);
    overflow: hidden;
  }
  .wave { position: absolute; left: 0; bottom: 0; width: 100%; display: block; }
  .wordmark {
    display: flex; align-items: center; gap: 6px;
    font-weight: 700; color: var(--brand); text-transform: uppercase;
    letter-spacing: .04em; line-height: 1.1;
  }
  .wordmark .dot { border-radius: 50%; background: var(--gold); flex: none; }
  .wordmark.on-dark { color: var(--paper); }

  /* business card front */
  .card-front { left: 20px; top: 28px; width: 200px; height: 115px; padding: 9px 10px; }
  .card-front .name { font-size: 10px; font-weight: 700; color: var(--navy); }
  .card-front .role { font-size: 6px; color: var(--ink-soft); margin-bottom: 5px; }
  .card-front .columns { display: flex; gap: 8px; font-size: 4.6px; line-height: 1.45; }
  .card-front .columns b { color: var(--navy); font-weight: 700; }
  .card-front .web { font-size: 4.6px; margin-top: 4px; line-height: 1.45; }
  .card-front .license { position: absolute; left: 10px; bottom: 6px; font-size: 4.4px; color: var(--paper); z-index: 2; }

  /* business card back */
  .card-back { left: 20px; top: 190px; width: 200px; height: 115px; }
  .card-back .wordmark { position: absolute; left: 0; right: 0; top: 32px; justify-content: center; font-size: 11px; }
  .card-back .wordmark .dot { width: 12px; height: 12px; }
  .card-back .affiliate { position: absolute; left: 0; right: 0; bottom: 6px; text-align: center; font-size: 6px; color: var(--paper); z-index: 2; font-weight: 600; }

  /* notebook cover */
  .notebook { left: 245px; top: 70px; width: 120px; height: 170px; }
  .notebook .wordmark { position: absolute; left: 0; right: 0; top: 50px; justify-content: center; font-size: 7px; text-align: center; }
  .notebook .wordmark .dot { width: 8px; height: 8px; }

  /* letterhead */
  .letterhead { left: 385px; top: 18px; width: 235px; height: 332px; padding: 16px 18px; }
  .letterhead .wordmark { justify-content: flex-end; font-size: 7px; }
  .letterhead .wordmark .dot { width: 8px; height: 8px; }
  .letterhead .contact { text-align: right; font-size: 4.2px; line-height: 1.5; margin-top: 4px; color: var(--ink-soft); }
  .letterhead .body { margin-top: 18px; font-size: 5px; line-height: 1.7; }
  .letterhead .body p { margin-bottom: 7px; }
  .letterhead .signature { font-weight: 700; color: var(--navy); }

  /* folder */
  .folder { left: 645px; top: 18px; width: 240px; height: 332px; background: var(--navy); }
  .folder .wordmark { position: absolute; left: 0; right: 0; top: 120px; justify-content: center; font-size: 12px; }
  .folder .wordmark .dot { width: 14px; height: 14px; }

  /* envelope */
  .envelope { left: 910px; top: 22px; width: 270px; height: 132px; padding: 12px 14px; }
  .envelope .wordmark { font-size: 7px; }
  .envelope .wordmark .dot { width: 8px; height: 8px; }
  .envelope .contact { font-size: 4.4px; line-height: 1.5; margin-top: 4px; color: var(--ink-soft); }

  /* disc */
  .disc { left: 975px; top: 178px; width: 150px; height: 150px; border-radius: 50%; }
  .disc .hole { position: absolute; left: 62px; top: 62px; width: 26px; height: 26px; border-radius: 50%; background: var(--stage); box-shadow: inset 0 1px 3px rgba(0,0,0,.2); }
  .disc .wordmark { position: absolute; left: 0; right: 0; top: 34px; justify-content: center; font-size: 6.5px; }
  .disc .wordmark .dot { width: 7px; height: 7px; }
</style>
</head>
<body>

<svg width="0" height="0" style="position:absolute">
  <defs>
    <symbol id="wave" viewBox="0 0 200 40" preserveAspectRatio="none">
      <path d="M0 16 C60 40 130 -2 200 10 L200 40 L0 40 Z" fill="#1c325e"/>
      <path d="M0 12 C60 36 130 -6 200 6" fill="none" stroke="#f2a81d" stroke-width="3"/>
    </symbol>
    <symbol id="wave-light" viewBox="0 0 200 40" preserveAspectRatio="none">
      <path d="M0 16 C60 40 130 -2 200 10 L200 40 L0 40 Z" fill="#ffffff"/>
      <path d="M0 12 C60 36 130 -6 200 6" fill="none" stroke="#f2a81d" stroke-width="3"/>
    </symbol>
  </defs>
</svg>

<section class="piece card-front" aria-label="Business card front">
  <p class="name">Melvor Tansley</p>
  <p class="role">Leisure and Business Travel Agent</p>
  <div class="columns">
    <div>
      <b>OakVale Court Office</b><br>
      418 Brindle Blvd., 4th Floor<br>
      Santa Monica, CA, 90408<br>
      Tel: 310-555-0193
    </div>
    <div>
      <b>Go Yonder Office</b><br>
      526 Fenwick Ave., #C<br>
      Santa Monica, CA, 90406<br>
      Tel: 310-555-0147 ext. 3871
    </div>
  </div>
  <p class="web">melvor@brightcompasstravelagency.example<br>www.brightcompasstravelagency.example</p>
  <svg class="wave" height="34"><use href="#wave"/></svg>
  <p class="license">Go Yonder Affiliate - CST# 2937516-82</p>
</section>

<section class="piece card-back" aria-label="Business card back">
  <div class="wordmark"><span class="dot"></span>Bright Compass Travel</div>
  <svg class="wave" height="34"><use href="#wave"/></svg>
  <p class="affiliate">Cobble Tours Affiliate</p>
</section>

<section class="piece notebook" aria-label="Notebook cover">
  <div class="wordmark"><span class="dot"></span>Bright Compass Travel</div>
  <svg class="wave" height="44"><use href="#wave"/></svg>
</section>

<section class="piece letterhead" aria-label="Letterhead">
  <div class="wordmark"><span class="dot"></span>Bright Compass Travel</div>
  <p class="contact">
    OakVale Court Office, 418 Brindle Blvd., 4th Floor, Santa Monica, CA, 90408 · Tel: 310-555-0193<br>
    Go Yonder Office, 526 Fenwick Ave., #C, Santa Monica, CA, 90406 · Tel: 310-555-0147 ext. 3871<br>
    www.brightcompasstravelagency.example
  </p>
  <div class="body">
    <p>Dear Guest,</p>
    <p>Thank you for choosing us for your next journey. Our team plans every trip with care, from quiet weekends to long business tours, so you can simply enjoy the road ahead.</p>
    <p>We look forward to hearing from you soon.</p>
    <p>Kind regards,<br><span class="signature">Melvor Tansley</span></p>
  </div>
  <svg class="wave" height="60"><use href="#wave"/></svg>
</section>

<section class="piece folder" aria-label="Presentation folder">
  <div class="wordmark on-dark"><span class="dot"></span>Bright Compass Travel</div>
  <svg class="wave" height="80"><use href="#wave-light"/></svg>
</section>

<section class="piece envelope" aria-label="Envelope">
  <div class="wordmark"><span class="dot"></span>Bright Compass Travel</div>
  <p class="contact">
    418 Brindle Blvd., 4th Floor<br>
    Santa Monica, CA, 90408<br>
    www.brightcompasstravelagency.example
  </p>
  <svg class="wave" height="36"><use href="#wave"/></svg>
</section>

<section class="piece disc" aria-label="Disc label">
  <div class="wordmark"><span class="dot"></span>Bright Compass Travel</div>
  <svg class="wave" height="52"><use href="#wave"/></svg>
  <span class="hole"></span>
</section>

</body>
</html>
```